CraneHollow - Business Card and Letterhead

After having received some fantastic submissions in our recent logo design project, I would now like to extend our branding to letterheads and business cards.
CraneHollow is a consulting service in the Construction Industry. We deal with both residential and commercial projects, and our clients include Architects, Builders, Tradespeople and Home Owners.
The designs should be simple and effective, convey personal service and professionalism, and display some level of creativity.
For both the business cards and letterhead, a white card stock will be used. This project is for business cards and letterheads only. Our new logo is attached for use.
The designs should incorporate our two main colours which are Blue (RGB 14,92,143) and Green (RGB 132,194,37).
For the time being, please submit all designs showing generic information including name, mobile number, email, postal address and website details. No fax number or physical address is required. I will provide our actual contact details once a final design has been selected.
I encourage you to interpret this brief in your own creative way, and look forward to some quality submissions.
Thanks!
Leo
CraneHollow.

```html
<!DOCTYPE html>
<html lang="en">
<head>
<meta charset="utf-8">
<title>CraneHollow – Business Card</title>
<link rel="stylesheet" href="https://fonts.googleapis.com/css2?family=Arimo:wght@400;700&display=swap">
<style>
  :root {
    --brand-blue: #2f5a8f;
    --brand-green: #84c225;
    --ink: #3a3a3a;
    --ink-soft: #6a6a6a;
    --rule: #6f6f6f;
    --card: #ffffff;
    --backdrop-top: #e9e9e9;
    --backdrop-bottom: #dcdcdc;
  }
  * { box-sizing: border-box; margin: 0; padding: 0; }
  html, body { width: 1200px; height: 800px; overflow: hidden; }
  body {
    background: linear-gradient(180deg, var(--backdrop-top), var(--backdrop-bottom));
    font-family: "Arimo", Arial, sans-serif;
    color: var(--ink);
    display: flex;
    align-items: center;
    justify-content: center;
    gap: 60px;
  }
  .card {
    position: relative;
    width: 500px;
    height: 286px;
    background: var(--card);
    box-shadow: 0 6px 18px rgba(0,0,0,0.12);
    overflow: hidden;
  }
  .card__stripe {
    position: absolute;
    left: 0; right: 0; bottom: 0;
    height: 10px;
    display: flex;
  }
  .card__stripe-blue { flex: 0 0 55%; background: var(--brand-blue); }
  .card__stripe-green { flex: 1; background: var(--brand-green); }

  .wordmark {
    display: flex;
    align-items: center;
    gap: 8px;
  }
  .wordmark__square {
    width: 24px; height: 24px;
    background: var(--brand-green);
  }
  .wordmark__name {
    font-weight: 700;
    color: var(--brand-blue);
    font-size: 29px;
    letter-spacing: -0.5px;
    line-height: 1;
  }

  /* Contact side */
  .card--contact { padding: 38px 34px 0; }
  .person { margin-top: 22px; }
  .person__name {
    color: var(--brand-blue);
    font-size: 15px;
    letter-spacing: 0.3px;
    text-transform: uppercase;
  }
  .person__role { font-size: 12px; color: var(--ink-soft); margin-top: 3px; }
  .divider {
    border: 0;
    border-top: 1px solid var(--rule);
    margin-top: 14px;
  }
  .details {
    display: flex;
    justify-content: space-between;
    margin-top: 14px;
    font-size: 11px;
    line-height: 17px;
    color: var(--ink-soft);
  }
  .details__label { color: var(--brand-blue); display: inline-block; width: 14px; }
  .details__postal { text-align: right; }
  .details__web-accent { color: var(--brand-green); }

  /* Logo side */
  .card--brand {
    display: flex;
    align-items: center;
    justify-content: center;
  }
  .card--brand .wordmark__square { width: 34px; height: 34px; }
  .card--brand .wordmark__name { font-size: 42px; }
</style>
</head>
<body>
  <article class="card card--contact">
    <div class="wordmark">
      <span class="wordmark__square"></span>
      <span class="wordmark__name">CraneHollow</span>
    </div>
    <div class="person">
      <p class="person__name">Ilsa Varnholt</p>
      <p class="person__role">Operation Manager</p>
    </div>
    <hr class="divider">
    <div class="details">
      <div class="details__direct">
        <p><span class="details__label">M</span>(555) 214 68 30</p>
        <p><span class="details__label">E</span>name@cranehollow.com</p>
      </div>
      <div class="details__postal">
        <p>PO Box 428 - Harbor City</p>
        <p>www.<span class="details__web-accent">cranehollow</span>.com</p>
      </div>
    </div>
    <div class="card__stripe"><span class="card__stripe-blue"></span><span class="card__stripe-green"></span></div>
  </article>

  <article class="card card--brand">
    <div class="wordmark">
      <span class="wordmark__square"></span>
      <span class="wordmark__name">CraneHollow</span>
    </div>
    <div class="card__stripe"><span class="card__stripe-blue"></span><span class="card__stripe-green"></span></div>
  </article>
</body>
</html>
```